Webdesign für Coaching von Erwachsenen und Kindern
Zielgruppe
Ich coache Erwachsene und Kinder mit den Methoden des NLP. Meine Zielgruppe sind primär Eltern und auch Lehrer. Mein Ziel sind mehr glückliche Kinder, indem ich primär die Eltern und teilweise auch die Kinder coache.
Mir ist es wichtig souverän und nicht wie eine Kindergärtnerin zu wirken.
Aufgabenstellung
Meine Website: www.coach-merlinger.ch ist mit Wordpress erstellt.
Das Logo besteht bereits und soll so belassen werden. Die Farben des Logos dürfen aufgegriffen werden. Es soll alles zusammenpassen und 'rund' wirken.
Mir gefällt zum Beispiel die Website lumaquo.ch oder Pflegewerk-nord.ch

```html
<!DOCTYPE html>
<html lang="de">
<head>
<meta charset="UTF-8">
<title>Lena Merlinger – Coaching</title>
<link href="https://fonts.googleapis.com/css2?family=Caveat+Brush&family=Montserrat:wght@400;500&display=swap" rel="stylesheet">
<style>
  :root {
    --bg: #eceff4;
    --navy: #0b3a80;
    --ink: #1b1b1f;
    --button: #1a80c6;
    --button-edge: #0d4a8a;
    --white: #ffffff;
  }
  * { margin: 0; padding: 0; box-sizing: border-box; }
  html, body { width: 1200px; height: 634px; overflow: hidden; }
  body {
    background: var(--bg);
    font-family: "Montserrat", Arial, sans-serif;
    color: var(--ink);
    position: relative;
  }
  .main-nav {
    position: absolute; left: 108px; top: 84px;
    display: flex; gap: 37px;
  }
  .main-nav a {
    font-size: 14.5px; color: var(--ink); text-decoration: none;
    padding-bottom: 5px; border-bottom: 2px solid transparent;
  }
  .main-nav a.is-active { border-bottom-color: var(--navy); }
  .brand {
    position: absolute; left: 602px; top: 95px;
    transform: translate(-50%, -50%);
    display: flex; align-items: center; gap: 10px;
    color: var(--navy); font-size: 24px; font-weight: 500;
    white-space: nowrap;
  }
  .brand-dot {
    width: 14px; height: 14px; border-radius: 50%;
    background: var(--button);
  }
  .contact-mail {
    position: absolute; left: 806px; top: 86px;
    display: flex; align-items: center; gap: 8px;
    font-size: 14.5px; color: var(--ink); text-decoration: none;
  }
  .hero-title {
    position: absolute; left: 104px; top: 152px;
    font-family: "Caveat Brush", cursive;
    font-weight: 400; font-size: 52px; line-height: 88px;
    color: var(--navy);
    white-space: nowrap;
  }
  .hero-lead {
    position: absolute; left: 107px; top: 423px; width: 560px;
    font-size: 14.3px; line-height: 22px;
  }
  .cta {
    position: absolute; left: 107px; top: 495px;
    width: 221px; height: 44px; border-radius: 22px;
    background: var(--button); border: 1.5px solid var(--button-edge);
    color: var(--white); font-size: 14px; font-weight: 500;
    display: flex; align-items: center; justify-content: center;
    text-decoration: none; text-transform: uppercase;
  }
  .hero-photo {
    position: absolute; left: 640px; top: 190px; width: 560px; height: 444px;
    background: radial-gradient(ellipse at 60% 60%, #ffffff 0%, #f7f8fa 45%, rgba(236,239,244,0) 72%);
  }
  .hero-photo-kids {
    position: absolute; left: 40px; top: 25px; width: 520px; height: 419px;
    background: radial-gradient(ellipse at 50% 55%, #f1d6c4 0%, #e8c6a8 35%, #f4f4f4 70%, rgba(255,255,255,0) 85%);
  }
</style>
</head>
<body>
  <nav class="main-nav">
    <a href="#">Angebote</a>
    <a href="#" class="is-active">Über Mich</a>
    <a href="#">Kontakt</a>
  </nav>

  <div class="brand"><span class="brand-dot"></span>Lena Merlinger</div>

  <a class="contact-mail" href="#">
    <svg width="14" height="11" viewBox="0 0 14 11" aria-hidden="true">
      <rect x="0.75" y="0.75" width="12.5" height="9.5" rx="1.5" fill="none" stroke="#0b3a80" stroke-width="1.5"/>
      <path d="M1.5 2 L7 6 L12.5 2" fill="none" stroke="#0b3a80" stroke-width="1.5"/>
    </svg>
    lena@coach-merlinger.ch
  </a>

  <h1 class="hero-title">Glückliche Kinder durch<br>entspannte Eltern, Lehrerinnen<br>und Lehrer</h1>

  <p class="hero-lead">Ich coache Eltern, Lehrerinnen und Lehrer und Kinder im Einzelsetting und biete Workshops für mehrere Personen an.</p>

  <a class="cta" href="#">Zum Kontakformular</a>

  <div class="hero-photo">
    <div class="hero-photo-kids" role="img" aria-label="Foto: zwei lächelnde Kinder, ein Junge und ein Mädchen, liegen nebeneinander auf den Armen"></div>
  </div>
</body>
</html>
```